Flyer-Design für Pflegeberatung
Zielgruppe
Ich würde gerne einen Flyer zur Pflegeberatung erstellen lassen. Zielgruppe sollen Senioren und Ihre Angehörigen sein.
Vielen Patienten benötigen eine Höherstufung des Pflegegrades oder bekommen keine Leistungen ausgezahlt ausgezahlt wenn Sie einen Pflegedienst beanspruchen. Hier benötigen wir einen originellen Flyer .
Aufgabenstellung
Ein kreativer und mutiger Flyer soll erstellt werden,
Es geht darum , dass wir die Leute beraten ,wie Sie mehr Pflegegeld bekommen.
Vielleicht können wir ein günstigeres Angebot unterbreiten, als der bisherige Pflegedienst.
Folgenden Text würde ich gerne einfügen:
Überschrift: Mehr Pflegegeld für Ihre Versorgung zu Hause
Reicht das Pflegegelt für Ihre Persönliche Versorgung nicht mehr aus?
Bleibt von Ihrem Pflegebudget kaum etwas für übrig?
Gerne beraten wir Sie zur Optimierung Ihrer Leistungen und planen gemeinsam, wie Sie trotz einer sehr guten Versorgung mehr Pflegegelt für sich behalten können.
Rufen Sie uns an,, wir beraten Sie sehr gerne telefonisch oder vereinbaren einen Beratungstermin bei Ihnen zu Hause.
Der Flyer wäre für zwei Pflegedienste zu erstellen.
Der Text und Grafik bleiben gleich, anzupassen wäre nur das Logo und die Adresse:
1. Adresse: Betreuungshaus Lindental GmbH, Kastanienweg 7 in 18432 Rostock, Tel 0381- 52146087
1. Adresse: hauskrankenpflege Velaris GmbH Birkenhainer Strasse 41 in Gnoien Tel 039971-541726

```html
<!DOCTYPE html>
<html lang="de">
<head>
<meta charset="utf-8">
<title>Mehr Pflegegeld für Ihre Versorgung zu Hause – Betreuungshaus Lindental</title>
<link rel="stylesheet" href="https://fonts.googleapis.com/css2?family=Open+Sans:wght@400;600;700&family=Ubuntu:ital,wght@1,700&display=swap">
<style>
  :root {
    --navy: #17234f;
    --blue: #2b84cc;
    --headline-blue: #2a8ad6;
    --orange: #f28a24;
    --white: #ffffff;
    --photo-a: #d9c6b4;
    --photo-b: #7fa7d4;
  }
  * { margin: 0; padding: 0; box-sizing: border-box; }
  html, body { width: 1200px; height: 800px; overflow: hidden; background: #e9eaea; }
  .flyer {
    position: relative;
    width: 1200px;
    height: 800px;
    background: var(--navy);
    overflow: hidden;
    font-family: "Open Sans", Arial, sans-serif;
    color: var(--white);
  }
  .shapes { position: absolute; inset: 0; }
  .headline {
    position: absolute; left: 52px; top: 38px;
    font-family: "Ubuntu", "Trebuchet MS", sans-serif;
    font-style: italic; font-weight: 700;
    font-size: 58px; line-height: 1.08;
  }
  .headline .accent { color: var(--headline-blue); }
  .questions {
    position: absolute; left: 62px; top: 250px; width: 520px;
    font-family: "Ubuntu", "Trebuchet MS", sans-serif;
    font-style: italic; font-weight: 700;
    font-size: 22px; line-height: 1.25;
    color: var(--orange);
  }
  .questions p + p { margin-top: 12px; }
  .intro {
    position: absolute; left: 62px; top: 400px; width: 380px;
    font-size: 22px; line-height: 1.45;
  }
  .photo { position: absolute; left: 450px; top: 320px; width: 470px; height: 480px; }
  .contact {
    position: absolute; left: 740px; top: 110px; width: 420px;
    text-align: center;
  }
  .contact__title {
    font-family: "Ubuntu", "Trebuchet MS", sans-serif;
    font-style: italic; font-weight: 700;
    font-size: 42px; color: var(--orange);
    margin-bottom: 10px;
  }
  .contact__text { font-size: 19px; line-height: 1.5; }
  .contact__details {
    margin-top: 44px; font-weight: 700; font-size: 19px; line-height: 1.75;
  }
  .brand {
    position: absolute; right: 40px; bottom: 40px; width: 300px;
    display: flex; flex-direction: column; align-items: center; gap: 14px;
  }
  .brand__mark {
    width: 90px; height: 90px; border-radius: 50%;
    border: 6px solid var(--white);
  }
  .brand__name {
    font-weight: 700; font-size: 24px; text-align: center; line-height: 1.2;
  }
</style>
</head>
<body>
<main class="flyer">
  <svg class="shapes" width="1200" height="800" viewBox="0 0 1200 800" aria-hidden="true">
    <path d="M 810 0 Q 570 150 530 560 L 530 800 L 1200 800 L 1200 0 Z" fill="var(--blue)" stroke="var(--white)" stroke-width="18"/>
    <path d="M 800 820 Q 870 650 1040 625 Q 1140 615 1220 645 L 1220 820 Z" fill="var(--navy)" stroke="var(--white)" stroke-width="18"/>
  </svg>

  <h1 class="headline">
    Mehr <span class="accent">Pflegegeld</span> für<br>
    Ihre <span class="accent">Versorgung</span><br>
    <span class="accent">zu Hause</span>
  </h1>

  <div class="questions">
    <p>Reicht das Pflegegelt für Ihre Persönliche Versorgung nicht mehr aus?</p>
    <p>Bleibt von Ihrem Budget kaum etwas für übrig?</p>
  </div>

  <p class="intro">Gerne beraten wir Sie zur Optimierung Ihrer Leistungen und planen gemeinsam, wie Sie trotz einer sehr guten Versorgung mehr Pflegegelt für sich behalten können</p>

  <svg class="photo" viewBox="0 0 470 480" role="img" aria-label="Foto: lächelnde Seniorin mit Brille hält fächerförmig Geldscheine in beiden Händen">
    <defs>
      <linearGradient id="photoTone" x1="0" y1="0" x2="0" y2="1">
        <stop offset="0" stop-color="var(--photo-a)"/>
        <stop offset="1" stop-color="var(--photo-b)"/>
      </linearGradient>
    </defs>
    <path d="M 60 480 L 60 200 Q 235 0 410 200 L 410 480 Z" fill="url(#photoTone)"/>
  </svg>

  <section class="contact">
    <h2 class="contact__title">Rufen Sie uns an!</h2>
    <p class="contact__text">wir beraten Sie sehr gerne telefonisch oder vereinbaren einen Beratungstermin bei Ihnen zu Hause</p>
    <address class="contact__details" style="font-style: normal;">
      Kastanienweg 7,<br>
      18432 Rostock<br>
      0381-52146087<br>
      info@betreuungshaus-lindental.de<br>
      www.betreuungshaus-lindental.de
    </address>
  </section>

  <div class="brand">
    <span class="brand__mark" aria-hidden="true"></span>
    <span class="brand__name">Betreuungshaus Lindental</span>
  </div>
</main>
</body>
</html>
```